43 Year Old Construction firm needs Updated Business Card & Stationery Design

We are an established and well known (in our market) commercial construction firm. We need a cleaner and more modern look for our corporate identity material. We would like to continue to use our current colors and logo.
We are thinking about incorporating a slogan on our business card (either front or back): "Striving to be the most trusted builder in our market." The text could change at some point. Our website is www.kradworth.example . Sample card is attached. Some will have more phone numbers, etc...
Updates

Target Market(s)

Commercial and institutional clients.

Industry/Entity Type

Construction Company

Contact Information for Business Card

See attached for existing card. But don't be constrained.

Requirements
Must have
• Logo, name, title, address, website, email, phone numbers (as few as one, as many as three)
• Slogan on front or back "Striving to be the most trusted builder in our market"
• Use existing logo and colors

```html
<!DOCTYPE html>
<html lang="en">
<head>
<meta charset="utf-8">
<title>Kradworth Builders — Business Card</title>
<link rel="stylesheet" href="https://fonts.googleapis.com/css2?family=Noto+Serif:wght@400;700&display=swap">
<style>
  :root {
    --brand-blue: #1d4f91;
    --brand-green: #1f9a4a;
    --card-white: #ffffff;
    --backdrop: #2b2b2d;
    --serif: "Noto Serif", Georgia, serif;
  }
  * { box-sizing: border-box; margin: 0; padding: 0; }
  html, body { width: 1200px; height: 900px; overflow: hidden; }
  body {
    background: var(--backdrop);
    font-family: var(--serif);
    position: relative;
  }
  .card {
    position: absolute;
    width: 682px;
    height: 390px;
    background: var(--card-white);
    box-shadow: 0 10px 24px rgba(0,0,0,.45);
    overflow: hidden;
  }
  .card--front { left: 150px; top: 40px; }
  .card--back  { left: 368px; top: 470px; }

  .wordmark {
    position: absolute;
    display: flex;
    align-items: center;
    gap: 12px;
    color: var(--brand-blue);
    font-weight: 700;
    line-height: 1;
    white-space: nowrap;
  }
  .wordmark__square {
    width: 28px; height: 28px;
    background: var(--brand-blue);
    flex: none;
  }
  .wordmark__name { font-size: 30px; letter-spacing: .3px; }

  .card--front .wordmark { left: 44px; top: 128px; }
  .website-line {
    position: absolute;
    right: 40px; top: 176px;
    font-size: 16px;
    color: var(--brand-blue);
    white-space: nowrap;
  }
  .slogan {
    position: absolute;
    right: 40px; bottom: 44px;
    font-size: 14px;
    letter-spacing: .3px;
    text-transform: uppercase;
    color: var(--brand-blue);
    white-space: nowrap;
  }
  .slogan__accent { color: var(--brand-green); }

  .card--back .wordmark { left: 44px; top: 66px; }
  .rule {
    position: absolute;
    left: 352px; right: 0; top: 196px;
    height: 2px;
    background: var(--brand-blue);
  }
  .person { position: absolute; left: 44px; top: 172px; }
  .person__name { font-size: 26px; font-weight: 700; color: var(--brand-blue); white-space: nowrap; }
  .person__title { font-size: 16px; color: var(--brand-green); margin-top: 2px; }
  .address {
    position: absolute; left: 64px; top: 246px;
    font-size: 16px; line-height: 1.3; color: var(--brand-blue); font-style: normal;
  }
  .contact-list {
    position: absolute; left: 64px; top: 300px;
    list-style: none; font-size: 16px; line-height: 1.3; color: var(--brand-blue);
  }
  .contact-list li { display: flex; align-items: center; gap: 8px; }
  .contact-list svg { width: 12px; height: 12px; flex: none; }
</style>
</head>
<body>

<section class="card card--front" aria-label="Card front">
  <div class="wordmark">
    <span class="wordmark__square"></span>
    <span class="wordmark__name">Kradworth Builders</span>
  </div>
  <p class="website-line">www.kradworth.example</p>
  <p class="slogan">Striving to be the most trusted <span class="slogan__accent">builder in our market</span></p>
</section>

<section class="card card--back" aria-label="Card back">
  <div class="wordmark">
    <span class="wordmark__square"></span>
    <span class="wordmark__name">Kradworth Builders</span>
  </div>
  <div class="rule"></div>
  <div class="person">
    <p class="person__name">Daniel R. Whitcombe</p>
    <p class="person__title">President</p>
  </div>
  <address class="address">
    4120 Larkspur Avenue<br>
    Fenmoor, MO 63000-1200
  </address>
  <ul class="contact-list">
    <li>
      <svg viewBox="0 0 12 12" aria-hidden="true"><path d="M2.5 1 L4.5 1 L5.2 3.6 L4 4.6 Q5 7 7.4 8 L8.4 6.8 L11 7.5 L11 9.5 Q10.5 11 9 11 Q1 10 1 3 Q1 1.5 2.5 1Z" fill="#1f9a4a"/></svg>
      Direct 555-201-4478
    </li>
    <li>
      <svg viewBox="0 0 12 12" aria-hidden="true"><rect x="1" y="2.5" width="10" height="7" fill="none" stroke="#1f9a4a" stroke-width="1.3"/><path d="M1 2.5 L6 6.5 L11 2.5" fill="none" stroke="#1f9a4a" stroke-width="1.3"/></svg>
      dwhitcombe@kradworth.example
    </li>
    <li>
      <svg viewBox="0 0 12 12" aria-hidden="true"><circle cx="6" cy="6" r="5" fill="none" stroke="#1f9a4a" stroke-width="1.2"/><ellipse cx="6" cy="6" rx="2.2" ry="5" fill="none" stroke="#1f9a4a" stroke-width="1"/><path d="M1 6 H11" stroke="#1f9a4a" stroke-width="1"/></svg>
      www.kradworth.example
    </li>
  </ul>
</section>

</body>
</html>
```